Travel Consultant Business Card

Hello.. New travel consultant looking seeking a business card that incorporates my new logo. I specialize in cruises but also want to imply land vacation. I am very open to any design and font concepts. I'm looking for a very upbeat modern design that reflects cruise and land vacations. Bright vibrant colors

Target Market(s)

Cruise and Land Vacationers

Industry/Entity Type

Travel Agent

Contact Information for Business Card

I am very open to any design and font concepts. I'm looking for a very upbeat modern design that reflects cruise and land vacations. Bright vibrant colors

Colors

Designer to choose colors to be used in the design.

Requirements
Must have
• Company Name: MapleRidge Journeys---New logo uploaded to be included in design
• My Name: Dolores Kwiatek-Travel Consultant
• Phone Number: (555) 418-7093
• E-Mail Address: mapleridgejourneys@examplemail.net
• Website: www.mapleridgejourneys.example
Nice to have
• My tag line is …..Here to Get You There

```html
<!DOCTYPE html>
<html lang="en">
<head>
<meta charset="utf-8">
<title>MapleRidge Journeys – Business Card</title>
<link href="https://fonts.googleapis.com/css2?family=Work+Sans:wght@400;500;700&display=swap" rel="stylesheet">
<style>
  :root {
    --backdrop: #262626;
    --card-blue: #1a5fad;
    --card-blue-light: #2369b6;
    --accent-cyan: #2ba6ea;
    --name-cyan: #45b4f2;
    --ink-white: #ffffff;
  }
  * { box-sizing: border-box; margin: 0; padding: 0; }
  html, body {
    width: 1200px; height: 900px; overflow: hidden;
    background: var(--backdrop);
    font-family: "Work Sans", Arial, sans-serif;
  }
  .sheet {
    width: 1200px; height: 900px;
    display: flex; flex-direction: column; align-items: center; justify-content: center;
    gap: 40px;
  }
  .card {
    position: relative;
    width: 700px; height: 400px;
    background: linear-gradient(135deg, var(--card-blue) 0%, var(--card-blue-light) 100%);
    border-bottom: 8px solid var(--accent-cyan);
    overflow: hidden;
  }
  .brand {
    display: flex; align-items: center; gap: 14px;
    color: var(--ink-white);
    font-weight: 700;
    line-height: 1.05;
  }
  .brand-mark {
    width: 18px; height: 18px; border-radius: 50%;
    background: var(--ink-white);
    flex: none;
  }
  .card-front .brand {
    position: absolute; left: 50%; top: 50%;
    transform: translate(-50%, -50%);
    font-size: 40px; white-space: nowrap;
  }
  .card-back .brand {
    position: absolute; left: 44px; top: 150px;
    width: 270px; font-size: 30px;
  }
  .divider {
    position: absolute; left: 340px; top: 100px;
    width: 2px; height: 200px;
    background: var(--accent-cyan);
  }
  .contact {
    position: absolute; left: 370px; top: 104px;
    color: var(--ink-white);
  }
  .contact-name {
    color: var(--name-cyan);
    font-weight: 700; font-size: 22px; letter-spacing: 1px;
    text-transform: uppercase;
  }
  .contact-role { font-size: 15px; margin-top: 4px; letter-spacing: .5px; }
  .contact-address { font-size: 15px; margin-top: 14px; line-height: 1.35; letter-spacing: .5px; }
  .contact-lines { list-style: none; margin-top: 14px; font-size: 14px; }
  .contact-lines li { display: flex; align-items: center; gap: 8px; line-height: 1.7; white-space: nowrap; }
  .contact-lines svg { width: 12px; height: 12px; flex: none; }
</style>
</head>
<body>
<main class="sheet">
  <section class="card card-front">
    <div class="brand"><span class="brand-mark"></span>MapleRidge Journeys</div>
  </section>

  <section class="card card-back">
    <div class="brand"><span class="brand-mark"></span>MapleRidge Journeys</div>
    <div class="divider"></div>
    <div class="contact">
      <p class="contact-name">Dolores Kwiatek</p>
      <p class="contact-role">Travel Consultant</p>
      <p class="contact-address">412b Harbour Lane,<br>Westbrook, NZ, 8023</p>
      <ul class="contact-lines">
        <li>
          <svg viewBox="0 0 12 12"><path d="M3 1 L5 3.5 L4 5 Q5 7 7 8 L8.5 7 L11 9 L9.5 11 Q4 10.5 1 3 Z" fill="var(--accent-cyan)"/></svg>
          (555) 418-7093
        </li>
        <li>
          <svg viewBox="0 0 12 12"><rect x="1" y="2.5" width="10" height="7" fill="none" stroke="var(--accent-cyan)" stroke-width="1.2"/><path d="M1 2.5 L6 6.5 L11 2.5" fill="none" stroke="var(--accent-cyan)" stroke-width="1.2"/></svg>
          mapleridgejourneys@examplemail.net
        </li>
        <li>
          <svg viewBox="0 0 12 12"><circle cx="6" cy="6" r="5" fill="none" stroke="var(--accent-cyan)" stroke-width="1.2"/><ellipse cx="6" cy="6" rx="2.2" ry="5" fill="none" stroke="var(--accent-cyan)" stroke-width="1"/><path d="M1 6 H11" stroke="var(--accent-cyan)" stroke-width="1"/></svg>
          www.mapleridgejourneys.example
        </li>
      </ul>
    </div>
  </section>
</main>
</body>
</html>
```